The Marrowvale

We need a APP for our members. this is a Private Bar/Venue. history of the brick building is it was built in1898 and was a gentleman club, oyster house, cigar factory and then law offices before we purchased and are beginning restoration.
the APP must include
1. direct texting to the concierge
2. calendar of events
3. veltrin Lock To open the lock, anyone with a code can approach the door, enable their phone's Bluetooth and press the relevant address from the app.
Read more: http://www.brevortgazette.co.uk/gadgetry/article-5182640/no-more-keys-phone-unlocks-your-front-door-from-anywhere.html#qwx8bRT2mkZp
4. Menus from various restaurants from our surrounding area
5. member name and member number to give the feel that the app is personalized
6. the members account balance
7. ability to pay their bill with credit card or zim tally monthly and automatically.
8. link to quöla with its own icon within the app.
9.the ability to reserve the room
Anything else that may of interest for our members that may be relevant that I may not have mentioned since we are new at this...
35 to 60 years of age
Club

```html
<!DOCTYPE html>
<html lang="en">
<head>
<meta charset="utf-8">
<title>The Marrowvale – Member App, Main Screen</title>
<link rel="stylesheet" href="https://fonts.googleapis.com/css2?family=Michroma&family=Roboto:wght@400;500;700&display=swap">
<style>
  :root {
    --page-bg: #ececec;
    --screen-bg-top: #202020;
    --screen-bg-bottom: #141414;
    --card-bg: #ffffff;
    --ink: #111111;
    --muted: #555555;
    --gold: #a8861f;
    --gold-text: #c09a2c;
    --gold-label: #b8922a;
    --white: #ffffff;
    --label-grey: #e4e4e4;
    --dash: #bdbdbd;
    --chat-blue: #2f8fd6;
  }
  * { margin: 0; padding: 0; box-sizing: border-box; }
  html, body { width: 1000px; height: 1200px; overflow: hidden; }
  body {
    background: var(--page-bg);
    font-family: "Roboto", Arial, sans-serif;
    position: relative;
  }
  .screen {
    position: absolute;
    left: 200px; top: 67px;
    width: 600px; height: 1065px;
    background: linear-gradient(180deg, var(--screen-bg-top), var(--screen-bg-bottom));
    overflow: hidden;
    color: var(--white);
  }
  .status-bar {
    position: absolute; left: 0; top: 0; width: 100%; height: 36px;
    font-size: 19px; font-weight: 500;
  }
  .status-bar .carrier { position: absolute; left: 12px; top: 6px; }
  .status-bar .clock { position: absolute; left: 0; width: 100%; top: 6px; text-align: center; }
  .status-bar .battery { position: absolute; right: 12px; top: 6px; display: flex; align-items: center; gap: 6px; }
  .battery-icon { width: 36px; height: 15px; border: 2px solid var(--white); border-radius: 3px; background: var(--white); position: relative; }
  .battery-icon::after { content: ""; position: absolute; right: -5px; top: 3px; width: 3px; height: 6px; background: var(--white); border-radius: 0 2px 2px 0; }

  .app-header { position: absolute; left: 0; top: 50px; width: 100%; height: 40px; }
  .menu-toggle { position: absolute; left: 26px; top: 4px; width: 30px; height: 32px; display: flex; flex-direction: column; justify-content: space-between; }
  .menu-toggle span { display: block; height: 5px; background: var(--white); }
  .app-title {
    position: absolute; left: 96px; top: 4px;
    font-family: "Michroma", "Roboto", sans-serif;
    font-size: 25px; letter-spacing: 5px; text-transform: uppercase;
  }

  .member-card {
    position: absolute; left: 25px; top: 118px; width: 550px; height: 347px;
    background: var(--card-bg); border-radius: 12px; color: var(--ink);
  }
  .member-avatar {
    position: absolute; left: 24px; top: 24px; width: 128px; height: 128px;
    border-radius: 50%; background: #222; display: flex; align-items: center; justify-content: center;
  }
  .member-name { position: absolute; left: 190px; top: 55px; font-size: 27px; font-weight: 500; letter-spacing: .3px; }
  .member-number { position: absolute; left: 190px; top: 92px; font-size: 27px; }
  .card-divider { position: absolute; left: 28px; right: 28px; top: 175px; border-top: 2px dashed var(--dash); }
  .card-notch { position: absolute; top: 163px; width: 26px; height: 26px; border-radius: 50%; background: var(--screen-bg-top); }
  .card-notch.left { left: -13px; }
  .card-notch.right { right: -13px; }
  .balance-label { position: absolute; left: 0; width: 100%; top: 196px; text-align: center; font-size: 19px; letter-spacing: 7px; color: #333; }
  .balance-amount { position: absolute; left: 0; width: 100%; top: 230px; text-align: center; font-size: 54px; font-weight: 700; }
  .balance-amount sup { font-size: 26px; vertical-align: 26px; margin-right: 6px; }

  .pay-button {
    position: absolute; left: 201px; top: 437px; width: 198px; height: 60px;
    background: var(--gold); border-radius: 30px; color: var(--white);
    font-size: 25px; font-weight: 500; letter-spacing: 1px;
    display: flex; align-items: center; justify-content: center;
  }

  .quick-links { position: absolute; left: 0; top: 560px; width: 100%; height: 120px; }
  .quick-link { position: absolute; width: 200px; text-align: center; }
  .quick-link svg { display: block; margin: 0 auto; }
  .quick-link .label { display: block; margin-top: 18px; font-size: 21px; color: var(--label-grey); text-transform: uppercase; }
  .quick-link.events { left: 0; }
  .quick-link.menus { left: 199px; }
  .quick-link.rides { left: 398px; }

  .reserve-room {
    position: absolute; left: 25px; top: 740px; width: 548px; height: 124px;
    border: 2px solid var(--gold); border-radius: 8px;
  }
  .reserve-room svg { position: absolute; left: 30px; top: 32px; }
  .reserve-room .label { position: absolute; left: 0; width: 100%; top: 46px; text-align: center; font-size: 27px; color: var(--gold-text); }

  .fab {
    position: absolute; top: 912px; width: 126px; height: 126px; border-radius: 50%;
    background: radial-gradient(circle at 50% 40%, #ffffff 60%, #e2e2e2 100%);
    display: flex; align-items: center; justify-content: center;
  }
  .fab.lock-access { left: 27px; }
  .fab.concierge { left: 447px; }
  .lock-access .brand-name { font-size: 22px; font-weight: 700; color: #e0232e; }
</style>
</head>
<body>
<main class="screen">
  <div class="status-bar">
    <span class="carrier">●●●●● Norvik</span>
    <span class="clock">7:28 AM</span>
    <span class="battery">100% <span class="battery-icon"></span></span>
  </div>

  <header class="app-header">
    <div class="menu-toggle" aria-label="Menu"><span></span><span></span><span></span></div>
    <h1 class="app-title">The Marrowvale</h1>
  </header>

  <section class="member-card">
    <div class="member-avatar">
      <svg width="64" height="64" viewBox="0 0 64 64" aria-hidden="true">
        <g fill="none" stroke="#b8922a" stroke-width="3">
          <path d="M24 14a8 8 0 0 1 16 0v10a8 8 0 0 1-16 0z"/>
          <path d="M26 34l-1 4-13 5c-2 1-3 3-3 5v6h46v-6c0-2-1-4-3-5l-13-5-1-4"/>
        </g>
      </svg>
    </div>
    <div class="member-name">DANIEL HARGROVE</div>
    <div class="member-number">0728</div>
    <span class="card-notch left"></span>
    <span class="card-notch right"></span>
    <div class="card-divider"></div>
    <div class="balance-label">BALANCE</div>
    <div class="balance-amount"><sup>$</sup>284.60</div>
  </section>

  <div class="pay-button">PAY</div>

  <nav class="quick-links">
    <div class="quick-link events">
      <svg width="58" height="58" viewBox="0 0 58 58" aria-hidden="true">
        <rect x="4" y="8" width="50" height="46" rx="5" fill="#b8922a"/>
        <rect x="14" y="2" width="6" height="12" rx="2" fill="#b8922a" stroke="#1c1c1c" stroke-width="2"/>
        <rect x="38" y="2" width="6" height="12" rx="2" fill="#b8922a" stroke="#1c1c1c" stroke-width="2"/>
        <rect x="9" y="18" width="40" height="31" fill="#1c1c1c"/>
        <g fill="#b8922a">
          <rect x="18" y="24" width="6" height="6"/><rect x="26" y="24" width="6" height="6"/><rect x="34" y="24" width="6" height="6"/>
          <rect x="18" y="33" width="6" height="6"/><rect x="26" y="33" width="6" height="6"/><rect x="34" y="33" width="6" height="6"/>
        </g>
      </svg>
      <span class="label">Events</span>
    </div>
    <div class="quick-link menus">
      <svg width="64" height="64" viewBox="0 0 64 64" aria-hidden="true">
        <circle cx="32" cy="32" r="28" fill="none" stroke="#b8922a" stroke-width="4"/>
        <ellipse cx="22" cy="24" rx="5" ry="8" fill="#b8922a"/>
        <rect x="20.5" y="28" width="3" height="22" fill="#b8922a"/>
        <path d="M29 14v12c0 3 2 4 3.5 4v20h3V30c1.5 0 3.5-1 3.5-4V14h-2v10h-1.5V14h-2v10H32V14z" fill="#b8922a"/>
        <path d="M44 14c-3 3-4 9-4 14h3v22h3V14z" fill="#b8922a"/>
      </svg>
      <span class="label">Nearby Menus</span>
    </div>
    <div class="quick-link rides">
      <svg width="58" height="58" viewBox="0 0 58 58" aria-hidden="true">
        <rect x="8" y="8" width="42" height="42" fill="#b8922a"/>
      </svg>
      <span class="label">quöla</span>
    </div>
  </nav>

  <div class="reserve-room">
    <svg width="50" height="60" viewBox="0 0 50 60" aria-hidden="true">
      <rect x="2" y="2" width="28" height="56" fill="#b8922a"/>
      <circle cx="24" cy="32" r="2.5" fill="#1c1c1c"/>
      <circle cx="40" cy="26" r="6" fill="none" stroke="#b8922a" stroke-width="3"/>
      <path d="M40 32v16M40 40h5M40 45h4" stroke="#b8922a" stroke-width="3" fill="none"/>
    </svg>
    <span class="label">RESERVE A ROOM</span>
  </div>

  <div class="fab lock-access" aria-label="veltrin Lock">
    <span class="brand-name">veltrin</span>
  </div>
  <div class="fab concierge" aria-label="Text the concierge">
    <svg width="70" height="60" viewBox="0 0 70 60" aria-hidden="true">
      <path d="M8 6h54a4 4 0 0 1 4 4v28a4 4 0 0 1-4 4H30l-12 12v-12H8a4 4 0 0 1-4-4V10a4 4 0 0 1 4-4z" fill="#ffffff" stroke="#2f8fd6" stroke-width="3"/>
      <g fill="#2f8fd6"><circle cx="22" cy="24" r="3.5"/><circle cx="35" cy="24" r="3.5"/><circle cx="48" cy="24" r="3.5"/></g>
    </svg>
  </div>
</main>
</body>
</html>
```